Powerpoint template for technical & business level presentations

Looking for a powerpoint template to use for professional business & technical presentations that will work well with the logo you designed for us.

Industry/Entity Type

Business

```html
<!DOCTYPE html>
<html lang="en">
<head>
<meta charset="utf-8">
<title>Presentation Template – Corvane Partners</title>
<link rel="stylesheet" href="https://fonts.googleapis.com/css2?family=Graduate&family=Open+Sans:wght@400;600&family=Cinzel:wght@400;700&display=swap">
<style>
  :root {
    --blue: #29a9e1;
    --blue-deep: #0f74b8;
    --band: #1c1c1c;
    --paper-light: #f1f1f1;
    --paper-mid: #dcdcdc;
    --ink: #2a2a2a;
    --white: #ffffff;
    --gray: #5b5c5e;
    --gray-dark: #3c3d3f;
    --green-dark: #0e9444;
    --green: #2db873;
    --teal: #15a89a;
    --lime: #8cc43f;
    --tan: #c49a6c;
  }
  * { box-sizing: border-box; margin: 0; padding: 0; }
  html, body { width: 1200px; height: 900px; overflow: hidden; background: var(--white); }
  body { position: relative; font-family: "Open Sans", sans-serif; color: var(--ink); }

  .sheet-icon {
    position: absolute; left: 17px; top: 8px; width: 140px; height: 140px;
    background: linear-gradient(135deg, var(--blue) 55%, var(--blue-deep) 55%);
  }

  .slide {
    position: absolute; overflow: hidden;
    background: radial-gradient(ellipse at 40% 40%, var(--paper-light), var(--paper-mid));
    box-shadow: 0 1px 3px rgba(0,0,0,.25);
  }
  .slide--title { left: 70px; top: 160px; width: 571px; height: 322px; }
  .slide--thanks { left: 67px; top: 502px; width: 574px; height: 330px; }
  .slide--graphic { left: 656px; top: 15px; width: 473px; height: 265px; }
  .slide--image { left: 656px; top: 292px; width: 473px; height: 265px; }
  .slide--bullets { left: 656px; top: 566px; width: 473px; height: 265px; }

  .display {
    font-family: "Graduate", serif; color: var(--blue);
    line-height: 1; white-space: nowrap; font-weight: 400;
  }
  .reflect {
    position: absolute; opacity: .35;
    -webkit-mask-image: linear-gradient(to top, #000 0%, transparent 70%);
    mask-image: linear-gradient(to top, #000 0%, transparent 70%);
  }

  .title-page__heading {
    position: absolute; left: 130px; top: 28px; font-size: 56px;
    transform: scaleX(.9); transform-origin: left top;
  }
  .title-page__heading.reflect { top: 92px; transform: scale(.9, -1); transform-origin: left center; }
  .title-page__sub { position: absolute; left: 138px; top: 81px; font-size: 11px; color: var(--ink); white-space: nowrap; }
  .title-page__sub.reflect { top: 95px; transform: scaleY(-1); }
  .title-page__badge {
    position: absolute; left: 237px; top: 156px; width: 118px; height: 118px; border-radius: 50%;
    background: var(--blue); border: 3px solid var(--white); box-shadow: 0 0 0 2px var(--blue);
    display: flex; align-items: center; justify-content: center;
  }
  .title-page__url { position: absolute; left: 197px; top: 291px; font-size: 12px; }

  .brand-name { font-family: "Graduate", serif; color: var(--white); white-space: nowrap; }
  .title-page__badge .brand-name { font-size: 13px; }

  .thanks__heading {
    position: absolute; left: 138px; top: 136px; font-size: 58px;
    transform: scaleX(.78); transform-origin: left top;
  }
  .thanks__heading.reflect { top: 196px; transform: scale(.78, -1); transform-origin: left center; }

  .corner { position: absolute; width: 48px; height: 48px; }
  .corner--bottom { right: 12px; bottom: 12px; }
  .corner--top { right: 6px; top: 3px; width: 42px; height: 42px; }
  .corner__label { font-family: "Graduate", serif; fill: var(--white); }

  .rule { position: absolute; left: 10px; top: 16px; }

  .band {
    position: absolute; left: 6px; right: 6px; bottom: 6px; height: 58px; background: var(--band);
  }
  .band__title {
    position: absolute; left: 10px; top: 8px; font-size: 28px; padding-bottom: 2px;
    border-bottom: 2px solid var(--white); transform: scaleX(.92); transform-origin: left top;
  }
  .band__detail { position: absolute; left: 33px; top: 43px; font-size: 7px; color: var(--white); white-space: nowrap; }
  .band__detail--short { left: 128px; }
  .band__contact { position: absolute; right: 86px; top: 36px; font-size: 5px; line-height: 7px; color: var(--white); text-align: right; }
  .band__brand { position: absolute; right: 6px; top: 36px; font-size: 10px; color: var(--blue); font-family: "Graduate", serif; }

  .graphic-pyramid { position: absolute; left: 30px; top: 70px; }
  .graphic-pie { position: absolute; left: 270px; top: 50px; }

  .image-frame { position: absolute; left: 10px; top: 13px; width: 198px; height: 176px; background: var(--band); }
  .image-frame__area {
    position: absolute; left: 6px; top: 8px; width: 164px; height: 164px;
    background: linear-gradient(135deg, var(--blue) 55%, var(--blue-deep) 55%);
  }
  .image-frame__caption {
    position: absolute; left: 181px; top: 88px; transform: translate(-50%, -50%) rotate(-90deg);
    font-size: 10.5px; color: var(--white); white-space: nowrap;
  }

  .bullets { position: absolute; left: 46px; top: 40px; font-family: "Cinzel", serif; list-style: none; }
  .bullets__main { font-family: "Graduate", serif; color: var(--blue); font-size: 18px; display: flex; align-items: center; gap: 8px; }
  .bullets__sub { margin: 6px 0 0 36px; list-style: none; }
  .bullets__sub li { font-size: 10px; display: flex; align-items: center; gap: 6px; height: 17px; margin-bottom: 6px; }
</style>
</head>
<body>

<div class="sheet-icon" role="img" aria-label="Image placeholder thumbnail"></div>

<section class="slide slide--title">
  <h1 class="display title-page__heading">TITLE PAGE</h1>
  <div class="display title-page__heading reflect" aria-hidden="true">TITLE PAGE</div>
  <p class="title-page__sub">DETAILS OF PRESENTATION / NAME OF PRESENTOR</p>
  <div class="title-page__badge"><span class="brand-name">CORVANE</span></div>
  <p class="title-page__url">http://www.companysite.com/</p>
  <svg class="corner corner--bottom" viewBox="0 0 48 48"><polygon points="0,48 48,48 48,0" fill="var(--blue)"/><text class="corner__label" x="36" y="44" font-size="17" text-anchor="middle">01</text></svg>
</section>

<section class="slide slide--thanks">
  <h2 class="display thanks__heading">THANK YOU</h2>
  <div class="display thanks__heading reflect" aria-hidden="true">THANK YOU</div>
  <svg class="corner corner--bottom" viewBox="0 0 48 48"><polygon points="0,48 48,48 48,0" fill="var(--blue)"/><text class="corner__label" x="37" y="44" font-size="18" text-anchor="middle">X</text></svg>
</section>

<section class="slide slide--graphic">
  <svg class="rule" width="410" height="14" viewBox="0 0 410 14"><circle cx="9" cy="7" r="6" fill="none" stroke="var(--blue)" stroke-width="1.5"/><circle cx="9" cy="7" r="3" fill="var(--blue)"/><line x1="16" y1="7" x2="408" y2="7" stroke="var(--ink)" stroke-width="1.5"/></svg>
  <svg class="corner corner--top" viewBox="0 0 42 42"><polygon points="0,0 42,0 42,42" fill="var(--blue)"/><text class="corner__label" x="29" y="17" font-size="11" text-anchor="middle">04</text></svg>
  <svg class="graphic-pyramid" width="200" height="120" viewBox="0 0 200 120">
    <polygon points="97,4 121,32 73,32" fill="var(--lime)"/>
    <rect x="73" y="32" width="48" height="5" fill="#6e9a30"/>
    <polygon points="66,39 128,39 148,59 40,59" fill="var(--blue)"/>
    <rect x="40" y="59" width="108" height="4" fill="var(--blue-deep)"/>
    <polygon points="54,73 149,73 192,105 4,105" fill="var(--gray)"/>
    <rect x="4" y="105" width="188" height="7" fill="var(--gray-dark)"/>
  </svg>
  <svg class="graphic-pie" width="150" height="160" viewBox="0 0 150 160">
    <circle cx="71" cy="78" r="68" fill="#6b5640"/>
    <g transform="rotate(-115 71 68)">
      <circle cx="71" cy="68" r="34" fill="none" stroke="var(--green-dark)" stroke-width="68" pathLength="100" stroke-dasharray="14 86" stroke-dashoffset="0"/>
      <circle cx="71" cy="68" r="34" fill="none" stroke="var(--green)" stroke-width="68" pathLength="100" stroke-dasharray="13 87" stroke-dashoffset="-14"/>
      <circle cx="71" cy="68" r="34" fill="none" stroke="var(--teal)" stroke-width="68" pathLength="100" stroke-dasharray="12 88" stroke-dashoffset="-27"/>
      <circle cx="71" cy="68" r="34" fill="none" stroke="var(--blue)" stroke-width="68" pathLength="100" stroke-dasharray="17 83" stroke-dashoffset="-39"/>
      <circle cx="71" cy="68" r="34" fill="none" stroke="var(--tan)" stroke-width="68" pathLength="100" stroke-dasharray="16 84" stroke-dashoffset="-56"/>
      <circle cx="71" cy="68" r="34" fill="none" stroke="var(--gray)" stroke-width="68" pathLength="100" stroke-dasharray="15 85" stroke-dashoffset="-72"/>
      <circle cx="71" cy="68" r="34" fill="none" stroke="var(--lime)" stroke-width="68" pathLength="100" stroke-dasharray="13 87" stroke-dashoffset="-87"/>
    </g>
    <circle cx="71" cy="68" r="68" fill="none" stroke="var(--band)" stroke-width="1.5"/>
  </svg>
  <div class="band">
    <h3 class="display band__title">GRAPHIC SLIDE</h3>
    <p class="band__detail">DETAILS OF SLIDE / NAME OF PRESENTOR</p>
    <p class="band__contact">WWW.COMPANYSITE.COM<br>COMPANY@COMPANYSITE.COM</p>
    <span class="band__brand">CORVANE</span>
  </div>
</section>

<section class="slide slide--image">
  <svg class="corner corner--top" viewBox="0 0 42 42"><polygon points="0,0 42,0 42,42" fill="var(--blue)"/><text class="corner__label" x="29" y="17" font-size="11" text-anchor="middle">02</text></svg>
  <div class="image-frame">
    <div class="image-frame__area" role="img" aria-label="Sample image placement"></div>
    <span class="image-frame__caption">sample image placement</span>
  </div>
  <div class="band">
    <h3 class="display band__title">SLIDE TITLE</h3>
    <p class="band__detail">DETAILS OF SLIDE / NAME OF PRESENTOR</p>
    <p class="band__contact">WWW.COMPANYSITE.COM<br>COMPANY@COMPANYSITE.COM</p>
    <span class="band__brand">CORVANE</span>
  </div>
</section>

<section class="slide slide--bullets">
  <svg class="rule" width="440" height="14" viewBox="0 0 440 14"><circle cx="9" cy="7" r="6" fill="none" stroke="var(--blue)" stroke-width="1.5"/><circle cx="9" cy="7" r="3" fill="var(--blue)"/><line x1="16" y1="7" x2="432" y2="7" stroke="var(--ink)" stroke-width="1.5"/></svg>
  <svg class="corner corner--top" viewBox="0 0 42 42"><polygon points="0,0 42,0 42,42" fill="var(--blue)"/><text class="corner__label" x="29" y="17" font-size="11" text-anchor="middle">03</text></svg>
  <ul class="bullets">
    <li>
      <span class="bullets__main"><svg width="16" height="16" viewBox="0 0 16 16"><polygon points="5,1 11,1 15,5 15,11 11,15 5,15 1,11 1,5" fill="none" stroke="var(--blue)" stroke-width="2.5"/></svg>MAIN BULLET</span>
      <ul class="bullets__sub">
        <li><svg width="13" height="13" viewBox="0 0 14 14"><polygon points="4,1 10,1 13,4 13,10 10,13 4,13 1,10 1,4" fill="var(--blue)" stroke="var(--band)" stroke-width="1.5"/></svg>SUB BULLET FORM</li>
        <li><svg width="13" height="13" viewBox="0 0 14 14"><polygon points="4,1 10,1 13,4 13,10 10,13 4,13 1,10 1,4" fill="var(--blue)" stroke="var(--band)" stroke-width="1.5"/></svg>SUB BULLET FORM</li>
        <li><svg width="13" height="13" viewBox="0 0 14 14"><polygon points="4,1 10,1 13,4 13,10 10,13 4,13 1,10 1,4" fill="var(--blue)" stroke="var(--band)" stroke-width="1.5"/></svg>SUB BULLET FORM</li>
      </ul>
    </li>
  </ul>
  <div class="band">
    <h3 class="display band__title">SLIDE TITLE</h3>
    <p class="band__detail band__detail--short">BULLET FORM</p>
    <p class="band__contact">WWW.COMPANYSITE.COM<br>COMPANY@COMPANYSITE.COM</p>
    <span class="band__brand">CORVANE</span>
  </div>
</section>

</body>
</html>
```